This will turn into a huge project with mass exposure.

Tallow Crest creates soap, perfumes, rubs, lotion, etc for some of the most know brands in the market: Marisol Veil, Fern & Pebble Supply, PGR sports teams, etc.

They are going to be redesigning all logos, labels, websites and print.

They are starting with a business card and logo.

ALL designs must include a logo for Tallow Crest Holdings
Updates

Target Market(s)

Purchasers such as Marisl Veil

Industry/Entity Type

Business

Requirements
Must have
• a space for Qr code

two sided

Info:
Gavin Torlek, President
info@tallowcrest.example
555-014-2783
Nice to have
• Colors: gray background with blue and green tones. A globe that looks like an ancient map.

```html
<!DOCTYPE html>
<html lang="en">
<head>
<meta charset="utf-8">
<title>Tallow Crest Holdings — Business Card</title>
<link rel="stylesheet" href="https://fonts.googleapis.com/css2?family=Poppins:wght@600&family=Questrial&display=swap">
<style>
  :root {
    --stage: #676767;
    --front-green: #9cc43a;
    --front-green-light: #b7d75a;
    --front-green-deep: #86b02c;
    --map-green: #a9cf4f;
    --back-paper: #f1f1f0;
    --back-paper-edge: #dedede;
    --map-gray: #e2e2e1;
    --brand-blue: #1d5f8c;
    --brand-green: #5cbf8a;
    --name-blue: #3ab4e6;
    --title-gray: #555555;
    --contact-teal: #1e6a8e;
    --qr-line: #b9b9b9;
    --globe-gold: #b98a2c;
    --globe-brown: #8a5f1c;
  }
  * { margin: 0; padding: 0; box-sizing: border-box; }
  html, body {
    width: 1200px;
    height: 960px;
    overflow: hidden;
    background: var(--stage);
  }
  .canvas {
    position: relative;
    width: 1200px;
    height: 960px;
    background: var(--stage);
    font-family: "Questrial", "Century Gothic", sans-serif;
  }
  .card {
    position: absolute;
    width: 729px;
    height: 445px;
    overflow: hidden;
  }

  /* Brand mark: name with a plain circle */
  .brand {
    position: absolute;
    display: flex;
    align-items: center;
    color: var(--brand-blue);
    line-height: 1;
    white-space: nowrap;
  }
  .brand__dot {
    flex: none;
    border-radius: 50%;
    background: var(--brand-green);
  }

  /* Front side */
  .card--front {
    left: 22px;
    top: 25px;
    background: radial-gradient(ellipse at 55% 45%, var(--front-green-light) 0%, var(--front-green) 55%, var(--front-green-deep) 100%);
  }
  .card--front .world-map {
    position: absolute;
    left: 20px;
    top: 10px;
    width: 690px;
    height: 420px;
    border-radius: 40%;
    background: radial-gradient(ellipse at center, var(--map-green) 0%, rgba(169, 207, 79, 0) 70%);
  }
  .brand--front {
    left: 40px;
    top: 112px;
    font-size: 48px;
  }
  .brand--front .brand__dot {
    width: 26px;
    height: 26px;
    margin-left: 16px;
  }

  /* Back side */
  .card--back {
    left: 448px;
    top: 493px;
    background: radial-gradient(ellipse at 50% 40%, #ffffff 0%, var(--back-paper) 60%, var(--back-paper-edge) 100%);
  }
  .card--back .world-map {
    position: absolute;
    left: 60px;
    top: 20px;
    width: 640px;
    height: 400px;
    border-radius: 40%;
    background: radial-gradient(ellipse at center, var(--map-gray) 0%, rgba(226, 226, 225, 0) 70%);
  }
  .qr-space {
    position: absolute;
    left: 78px;
    top: 40px;
    width: 104px;
    height: 104px;
    border: 2px dashed var(--qr-line);
    background: rgba(255, 255, 255, 0.6);
  }
  .brand--back {
    right: 42px;
    top: 128px;
    font-size: 28px;
  }
  .brand--back .brand__dot {
    width: 14px;
    height: 14px;
    margin-left: 10px;
  }
  .contact {
    position: absolute;
    left: 78px;
    top: 186px;
  }
  .contact__name {
    font-family: "Poppins", "Century Gothic", sans-serif;
    font-weight: 600;
    font-size: 36px;
    line-height: 1;
    color: var(--name-blue);
  }
  .contact__role {
    margin-top: 10px;
    font-size: 43px;
    line-height: 1;
    letter-spacing: 3px;
    color: var(--title-gray);
  }
  .contact__details {
    margin-top: 32px;
    font-family: "Poppins", "Century Gothic", sans-serif;
    font-weight: 600;
    font-size: 22px;
    line-height: 34px;
    letter-spacing: 2px;
    color: var(--contact-teal);
  }
  .globe-area {
    position: absolute;
    left: 538px;
    top: 238px;
    width: 194px;
    height: 194px;
    background: linear-gradient(135deg, var(--globe-gold) 0%, var(--globe-brown) 100%);
  }
</style>
</head>
<body>
<main class="canvas">

  <section class="card card--front" aria-label="Business card, front">
    <div class="world-map" role="img" aria-label="Faint antique world map in soft green tones"></div>
    <p class="brand brand--front">Tallow Crest Holdings<span class="brand__dot"></span></p>
  </section>

  <section class="card card--back" aria-label="Business card, back">
    <div class="world-map" role="img" aria-label="Faint antique world map in pale gray tones"></div>
    <div class="qr-space" role="img" aria-label="Space reserved for a QR code"></div>
    <p class="brand brand--back">Tallow Crest Holdings<span class="brand__dot"></span></p>

    <div class="contact">
      <h1 class="contact__name">Gavin Torlek</h1>
      <p class="contact__role">President</p>
      <p class="contact__details">
        info@tallowcrest.example<br>
        555-014-2783
      </p>
    </div>

    <div class="globe-area" role="img" aria-label="Antique golden globe showing the continents"></div>
  </section>

</main>
</body>
</html>
```